One pager digital ad-Corporate travel Manager

I need a design that is smooth, and business like. I don’t like basic generic designs that I can make my self. I’m looking for a sharp clean ad that clearly was made by a great designer. I need some bullet points in and the add to be clean. Here is a list of some content from our content writers. You can arrange and play with the words a bit.

*Budget*- having a travel management service will ensure that your company sticks to a budget which will help PROTECT your bottom line. Travel expenses often CAN BE COSTLY and having a SAVVY corporate travel manager handle YOUR TRAVEL ARRANGEMENTS will make sure that the travel expenses are kept under control.
*Efficiency- time *is money. Have your staff focus on their core business and have the corporate travel manager handle all the logistics for their travel including airfare, hotel cars and events TO MAXIMIZE EFFICIENCY AND KEEP YOUR STAFF FOCUSED ON YOUR CORE BUSINESS

*unforeseen circumstances* – the corporate travel manager handleS any cancellations, missed flights, canceled flights. Quick rebooking, and repositioning, and dealing with getting credits and reimbursement is extremely difficult and time-consuming. The corporate travel manager handles all of that SO YOU CAN CONTINUE ON SCHEDULE WITHOUT SPENDING HOURS REBOOKING AND GETTING CREDIT

Efficient and organized business travel management-help reduce travel expenses, streamline expense reports, optimize booking processes, and make managing the corporate travel experience way easier for all stakeholders involved.

Travel Support

Report on travel spend: In order to optimize their budgets, businesses need to know which departments are spending what on travel. Agencies can report on spend for all stakeholders by team, department, or project, and help you accurately track all your travel expenses.

Maintain compliance: Every company has some sort of rules that make up their travel policy. An agency can enforce these guidelines when booking.

Velmora Journeys is a global leader in business travel management services. We drive savings, efficiency and safety to businesses and their travelers all around the world.

If you are looking for a tailored travel management solution, delivering customer service excellence, and a demonstrable return on investment, then you’ve come to the right place

Corporate travel policy compliance
Travel management reports
Meetings and event management
Travel program management
Dedicated travel counselor teams

By listening to your needs and focusing on your goals we can help your company design a global corporate travel service program that controls costs, improves traveler satisfaction and fits your corporate culture.

Our qualified business travel agents and cutting-edge technology deliver solutions that provide the best travel arrangements and travel policy adherence in the business. From CEO to support staff, our services can help make corporate travel a more efficient and enjoyable experience for everyone involved.

With so much involved in travel – from booking and expenses to meetings and strategy – you need the backing of a proven leader…
Velmora Journeys, We’re your corporate travel partner to help you manage it all.

```html
<!DOCTYPE html>
<html lang="en">
<head>
<meta charset="UTF-8">
<title>Velmora Journeys – Travel Management Service</title>
<link href="https://fonts.googleapis.com/css2?family=Poppins:wght@400;500;600;700&display=swap" rel="stylesheet">
<style>
:root{
  --navy:#0b1a45;
  --navy-deep:#081436;
  --ice:#cfeaf5;
  --text:#3c3f48;
  --white:#ffffff;
  --page:#e8e9eb;
  --rule:#3a4a78;
}
*{margin:0;padding:0;box-sizing:border-box}
html,body{width:1200px;height:3226px;overflow:hidden;background:var(--page);font-family:'Poppins',sans-serif;color:var(--text)}
.flyer{position:absolute;left:60px;top:850px;width:1080px;height:1527px;background:var(--white);overflow:hidden;box-shadow:0 6px 24px rgba(0,0,0,.12)}
.abs{position:absolute}
.header-bg{left:0;top:0;width:1080px;height:495px}
.brand{left:0;top:128px;width:430px;text-align:center;color:var(--white)}
.brand-mark{width:14px;height:14px;border:2px solid var(--white);border-radius:50%;display:inline-block;margin-bottom:12px}
.brand-name{font-size:25px;font-weight:400;letter-spacing:3px;text-transform:uppercase;line-height:1.2}
.title{left:66px;top:222px;color:var(--white);line-height:1}
.title-main{font-size:92px;font-weight:700;color:var(--ice);letter-spacing:1px}
.title-sub{font-size:55px;font-weight:500;letter-spacing:1px;margin-top:4px;line-height:1.07}
.tagline{left:66px;top:455px;font-size:28px;font-weight:700;color:var(--navy)}
.photo{left:0;top:0}
.feature-head{display:flex;align-items:center;position:absolute;left:66px}
.feature-icon{width:56px;height:56px;border-radius:50%;background:var(--white);border:3px solid var(--navy);display:flex;align-items:center;justify-content:center;position:relative;z-index:2}
.feature-label{background:var(--navy);color:var(--white);font-weight:500;font-size:25px;line-height:1.05;padding:8px 40px 8px 34px;margin-left:-22px;clip-path:polygon(0 0,calc(100% - 22px) 0,100% 100%,0 100%);position:relative}
.copy{position:absolute;left:66px;width:440px;font-size:14.2px;line-height:1.2}
.copy strong{font-weight:700;color:var(--navy-deep)}
.support{left:541px;top:533px;width:489px;height:692px;background:var(--navy)}
.support-title{left:589px;top:537px;width:393px;height:46px;background:var(--ice);clip-path:polygon(0 0,100% 0,93% 100%,7% 100%);text-align:center;font-weight:700;font-size:26px;color:var(--navy);line-height:46px}
.support-text{position:absolute;left:589px;width:405px;color:var(--white);font-size:14px;line-height:1.2}
.support-text strong{font-weight:700;text-transform:uppercase}
.divider{position:absolute;left:589px;width:405px;border-top:1px dashed var(--rule)}
.services{left:552px;top:1001px;width:470px;height:213px;background:var(--white)}
.service{position:absolute;text-align:center;font-size:13.5px;line-height:1.2;color:#4a4e58;width:150px}
.service-icon{width:46px;height:46px;margin:0 auto 6px;background:var(--ice)}
.vline{position:absolute;border-left:1px solid #d6dbe4}
.wide-copy{position:absolute;left:66px;width:964px;font-size:14.2px;line-height:1.2}
.wide-copy strong{font-weight:700;color:var(--navy-deep)}
.cta{left:66px;top:1387px;width:964px;height:65px;background:var(--navy)}
.cta-line{left:66px;top:1412px;width:964px;text-align:center;color:var(--white);font-weight:600;font-size:22px}
.pill{position:absolute;top:1368px;height:42px;background:var(--ice);display:flex;align-items:center;font-size:13.5px;font-weight:600;line-height:1.1;color:var(--navy);padding-left:50px}
.pill-num{position:absolute;left:10px;top:6px;width:30px;height:30px;border-radius:50%;background:var(--white);border:2px solid var(--navy);font-size:12px;font-weight:600;display:flex;align-items:center;justify-content:center}
.footer-tab{left:318px;top:1462px;width:440px;height:65px;background:var(--navy);clip-path:polygon(0 0,100% 0,88% 100%,12% 100%)}
.footer-rule{left:0;top:1522px;width:1080px;height:5px;background:var(--navy)}
.web{left:318px;top:1480px;width:440px;text-align:center;color:var(--white);font-weight:700;font-size:15px;letter-spacing:5px}
</style>
</head>
<body>
<main class="flyer">
  <svg class="abs header-bg" width="1080" height="495" viewBox="0 0 1080 495">
    <rect x="0" y="0" width="1080" height="441" fill="#0b1a45"/>
    <rect x="0" y="441" width="620" height="68" fill="#cfeaf5"/>
  </svg>
  <svg class="abs photo" width="1080" height="495" viewBox="0 0 1080 495">
    <defs>
      <linearGradient id="city" x1="0" y1="0" x2="0" y2="1">
        <stop offset="0" stop-color="#e4f2f8"/>
        <stop offset=".55" stop-color="#9fb4c6"/>
        <stop offset="1" stop-color="#6f8598"/>
      </linearGradient>
    </defs>
    <polygon points="580,0 492,224 570,495 596,495 518,224 606,0" fill="#cfeaf5"/>
    <polygon role="img" aria-label="Business traveller with a suitcase stepping out of a large phone screen in front of a city skyline" points="606,0 518,224 596,495 1080,495 1080,0" fill="url(#city)"/>
  </svg>

  <div class="abs brand">
    <span class="brand-mark"></span>
    <div class="brand-name">Velmora Journeys</div>
  </div>
  <div class="abs title">
    <div class="title-main">TRAVEL</div>
    <div class="title-sub">MANAGEMENT<br>SERVICE</div>
  </div>
  <div class="abs tagline">ADDING A JOY TO YOUR JOURNEY</div>

  <div class="feature-head" style="top:534px">
    <div class="feature-icon"><svg width="30" height="30" viewBox="0 0 30 30" fill="none" stroke="#0b1a45" stroke-width="2"><circle cx="17" cy="10" r="7"/><path d="M3 22h7l6 3 10-6"/></svg></div>
    <div class="feature-label">BUDGET</div>
  </div>
  <p class="copy" style="top:609px">having a travel management service will ensure that your company sticks to a budget which will help <strong>PROTECT</strong> your bottom line. Travel expenses often CAN BE COSTLY and having a <strong>SAVVY</strong> corporate travel manager handle YOUR <strong>TRAVEL ARRANGEMENTS</strong> will make sure that the travel expenses are kept under control.</p>

  <div class="feature-head" style="top:724px">
    <div class="feature-icon"><svg width="30" height="30" viewBox="0 0 30 30" fill="none" stroke="#0b1a45" stroke-width="2"><circle cx="15" cy="15" r="11"/><path d="M15 8v7l5 3"/></svg></div>
    <div class="feature-label">EFFICIENCY- TIME</div>
  </div>
  <p class="copy" style="top:801px">*Efficiency- time *is money. Have your staff focus on their core business and have the corporate travel manager handle all the logistics for their travel including airfare, hotel cars and events <strong>TO MAXIMIZE EFFICIENCY AND KEEP YOUR STAFF FOCUSED ON YOUR CORE BUSINESS</strong></p>

  <div class="feature-head" style="top:905px">
    <div class="feature-icon"><svg width="30" height="30" viewBox="0 0 30 30" fill="none" stroke="#0b1a45" stroke-width="2"><rect x="5" y="9" width="20" height="14" rx="2"/><path d="M11 9V6h8v3M5 15h20"/></svg></div>
    <div class="feature-label">*UNFORESEEN<br>CIRCUMSTANCES*</div>
  </div>
  <p class="copy" style="top:993px">*unforeseen circumstances* – the corporate travel manager handleS any cancellations, missed flights, canceled flights. Quick rebooking, and repositioning, and dealing with getting credits and reimbursement is extremely difficult and time-consuming. The corporate travel manager handles all of that <strong>SO YOU CAN CONTINUE ON SCHEDULE WITHOUT SPENDING HOURS REBOOKING AND GETTING CREDIT</strong></p>

  <p class="copy" style="top:1140px"><strong>Efficient and organized business travel management</strong>-help reduce travel expenses, streamline expense reports, optimize booking processes, and make managing the corporate travel experience way easier for all stakeholders involved.</p>

  <div class="abs support"></div>
  <div class="abs support-title">TRAVEL SUPPORT</div>
  <p class="support-text" style="top:606px"><strong>Report on travel spend:</strong><br>In order to optimize their budgets, businesses need to know which departments are spending what on travel. Agencies can report on spend for all stakeholders by team, department, or project, and help you accurately track all your travel expenses.</p>
  <div class="divider" style="top:720px"></div>
  <p class="support-text" style="top:732px"><strong>Maintain compliance:</strong><br>Every company has some sort of rules that make up their travel policy. An agency can enforce these guidelines when booking.</p>
  <div class="divider" style="top:810px"></div>
  <p class="support-text" style="top:822px">Velmora Journeys is a global leader in business travel management services. We drive savings, efficiency and safety to businesses and their travelers all around the world.</p>
  <div class="divider" style="top:898px"></div>
  <p class="support-text" style="top:909px">If you are looking for a tailored travel management solution, delivering customer service excellence, and a demonstrable return on investment, then you've come to the right place</p>

  <div class="abs services"></div>
  <div class="vline" style="left:704px;top:1016px;height:72px"></div>
  <div class="vline" style="left:856px;top:1016px;height:72px"></div>
  <div class="vline" style="left:786px;top:1110px;height:85px"></div>
  <div class="service" style="left:555px;top:1015px"><div class="service-icon"></div>Corporate travel policy compliance</div>
  <div class="service" style="left:710px;top:1015px"><div class="service-icon"></div>Travel management reports</div>
  <div class="service" style="left:864px;top:1015px"><div class="service-icon"></div>Meetings and event management</div>
  <div class="service" style="left:636px;top:1112px"><div class="service-icon"></div>Travel program management</div>
  <div class="service" style="left:805px;top:1112px"><div class="service-icon"></div>Dedicated travel counselor teams</div>

  <p class="wide-copy" style="top:1236px"><strong>By listening to your needs and focusing on your goals</strong> we can help your company design a global corporate travel service program that controls costs, improves traveler satisfaction and fits your corporate culture.</p>
  <p class="wide-copy" style="top:1286px"><strong>Our qualified business travel agents and cutting</strong>-edge technology deliver solutions that provide the best travel arrangements and travel policy adherence in the business. From CEO to support staff, our services can help make corporate travel a more efficient and enjoyable experience for everyone involved.</p>

  <div class="abs cta"></div>
  <div class="pill" style="left:114px;width:254px"><span class="pill-num">01</span>With so much involved<br>in travel</div>
  <div class="pill" style="left:402px;width:264px"><span class="pill-num">02</span>From booking and expenses<br>to meetings and strategy</div>
  <div class="pill" style="left:700px;width:280px"><span class="pill-num">03</span>You need the backing of<br>a proven leader...</div>
  <div class="abs cta-line">Velmora Journeys, We're your corporate travel partner to help you manage it all.</div>

  <div class="abs footer-rule"></div>
  <div class="abs footer-tab"></div>
  <div class="abs web">www.velmorajourneys.com</div>
</main>
</body>
</html>
```